Boracay Wedding Invitation Design

Hello, We would like a wedding invitation design for our wedding in Boracay. We would like it somewhat in the form of a boarding pass with beachy fresh colours, possibly a nice Boracay beach in the background Double sided with an envelope design to match. Maybe something simple on the envelope like a nice picture in the bottom left corner of a shell on a beach or something similar.

I would also like on the opposite side of the invite to be an "information sheet" with a matching beach design

The text files for both sides are included and i have also included 2 designs that i thought looked nice and are similar to what we are after.
Updates

Hello, I have updated the brief to be more specific with text files and images to make it easier for you. Thank you :)

Industry/Entity Type

Wedding

Font styles to use
Decorative
Script

Colors
fbee3d
33a6d7
33b8a4
fbf289
85cae6
ffffff

Requirements
Must have
• I would like to have this quote somewhere on the invitation
• This day I will marry my best friend,
• the one I laugh with,
• live for,
• dream with,
• love
• Owen & Marisa
• Request the pleasure of your company to celebrate their wedding
• On Friday the 17th March 2017
• at
• Velunda Grand Suites
• Boracay, Philippines
• Ceremony begins at 3.00pm
• RSVP
• Owen 0431907254
• Marisa 0417283649
• by
• 17th Jan 2016
• Dress: Beach Formal
• For the "information sheet"
• There will be a 5% discount on rooms booked at the Velunda under the event Owen & Marisa Wedding. The resort has a total of 24 rooms it would be nice if the majority of guests could stay at the resort from the night before until the night after the wedding but if you choose to stay elsewhere on the island there are plenty of other places to stay for cheaper and everything is fairly close as its a small island.
• We have currently blocked room stay for a short period of time so our guests can book rooms. If you choose to do so please email reservations@velundastays.example. Once rooms become available to the public again, towards the end of Jan, it will be first come first served basis. The resort is very popular so im assuming once this happens the rooms will be booked out.
• If you would like to check out the resort itself the website is www.velundagrand-isle.example
• We know its a fair distance to travel but we would really love to see you all there to celebrate and maybe even enjoy a small holiday while your here its a beautiful part of the world.
• If anyone has any questions please feel free to contact Owen on 0431907254
Nice to have
• A nice picture of a Boracay beach in the background would be nice

```html
<!DOCTYPE html>
<html lang="en">
<head>
<meta charset="utf-8">
<title>Owen &amp; Marisa — Wedding Invitation</title>
<link href="https://fonts.googleapis.com/css2?family=Cinzel:wght@400;500&family=Sorts+Mill+Goudy:ital@0;1&family=Raleway:wght@300&family=Great+Vibes&display=swap" rel="stylesheet">
<style>
  :root {
    --page: #e8e8e8;
    --sea-top: #86dde6;
    --sea-mid: #c4ecee;
    --sand: #f3f1e9;
    --ink-deep: #1e6db0;
    --ink: #2b86c9;
    --ink-soft: #5cb3dc;
    --script: #63bde3;
    --shadow: rgba(0,0,0,0.28);
  }
  * { margin: 0; padding: 0; box-sizing: border-box; }
  html, body { width: 1200px; height: 1200px; overflow: hidden; background: var(--page); }
  .canvas { position: relative; width: 1200px; height: 1200px; }

  .card {
    position: absolute; left: 60px; width: 1082px; height: 510px;
    background: linear-gradient(172deg, var(--sea-top) 0%, var(--sea-mid) 40%, var(--sand) 100%);
    box-shadow: 8px 9px 10px var(--shadow);
    overflow: hidden;
    color: var(--ink-deep);
  }
  .card--invite { top: 60px; }
  .card--info { top: 630px; }

  .line { position: absolute; left: 0; width: 100%; text-align: center; white-space: nowrap; }

  .quote { top: 52px; font-family: 'Raleway', sans-serif; font-weight: 300; font-size: 25px; color: var(--ink-soft); letter-spacing: 0.2px; }
  .quote .script { font-family: 'Great Vibes', cursive; font-size: 44px; color: var(--script); }

  .couple { top: 146px; font-family: 'Cinzel', serif; font-size: 40px; letter-spacing: 1px; }
  .couple .amp { font-family: 'Great Vibes', cursive; font-size: 52px; color: var(--ink); }
  .request { top: 196px; font-family: 'Cinzel', serif; font-size: 18px; letter-spacing: 3.2px; }
  .date { top: 230px; font-family: 'Cinzel', serif; font-size: 16.5px; letter-spacing: 2.6px; color: var(--ink); }
  .at { top: 261px; font-family: 'Sorts Mill Goudy', serif; font-style: italic; font-size: 20px; }
  .venue { top: 293px; font-family: 'Cinzel', serif; font-size: 18px; letter-spacing: 2.8px; }
  .place { top: 316px; font-family: 'Sorts Mill Goudy', serif; font-style: italic; font-size: 22px; color: var(--ink); letter-spacing: 0.5px; }
  .details { font-family: 'Cinzel', serif; font-size: 17px; letter-spacing: 1.8px; color: var(--ink); }
  .details span + span { margin-left: 26px; }
  .details--ceremony { top: 402px; }
  .details--rsvp { top: 443px; }

  .beach-photo { position: absolute; left: 26px; top: 26px; width: 468px; height: 366px; }

  .info-title { position: absolute; left: 542px; top: 26px; font-family: 'Cinzel', serif; font-size: 27px; letter-spacing: 4px; color: var(--ink); }
  .info-col { position: absolute; top: 70px; width: 256px; font-family: 'Sorts Mill Goudy', serif; font-size: 15px; line-height: 27.8px; color: var(--ink-deep); }
  .info-col--left { left: 542px; }
  .info-col--right { left: 812px; }
  .info-col p { text-indent: 26px; margin-bottom: 5px; }

  .website { top: 420px; font-family: 'Sorts Mill Goudy', serif; font-size: 13.5px; font-variant: small-caps; letter-spacing: 0.6px; color: var(--ink); }
  .closing { position: absolute; left: 28px; right: 28px; top: 450px; text-align: center; font-family: 'Sorts Mill Goudy', serif; font-size: 15px; line-height: 22px; color: var(--ink-deep); }
</style>
</head>
<body>
<main class="canvas">
  <section class="card card--invite" aria-label="Invitation front">
    <p class="line quote">This day I will marry my <span class="script">Best friend</span> the one I <span class="script">laugh</span> with, <span class="script">live</span> for, <span class="script">dream</span> with, <span class="script">love</span></p>
    <h1 class="line couple">OWEN <span class="amp">&amp;</span> MARISA</h1>
    <p class="line request">REQUEST THE PLEASURE OF YOUR COMPANY TO CELEBRATE THEIR WEDDING</p>
    <p class="line date">ON FRIDAY THE 17TH MARCH 2017</p>
    <p class="line at">at</p>
    <p class="line venue">VELUNDA GRAND SUITES</p>
    <p class="line place">Boracay, Philippines</p>
    <p class="line details details--ceremony"><span>CEREMONY BEGINS AT 3.00PM</span><span>DRESS: BEACH FORMAL</span></p>
    <p class="line details details--rsvp"><span>RSVP</span><span>OWEN 0431 907 254</span><span>MARISA 0417 283 649</span><span>BY 17TH JAN 2016</span></p>
  </section>

  <section class="card card--info" aria-label="Information sheet">
    <svg class="beach-photo" role="img" aria-label="Photo of a palm-lined white sand beach with umbrellas, loungers and turquoise sea" viewBox="0 0 468 366" preserveAspectRatio="none">
      <defs>
        <linearGradient id="beachTones" x1="0" y1="0" x2="0" y2="1">
          <stop offset="0" stop-color="#5c93e6"/>
          <stop offset="0.35" stop-color="#dbe8f5"/>
          <stop offset="0.55" stop-color="#6fc3c9"/>
          <stop offset="0.7" stop-color="#e9e4da"/>
          <stop offset="1" stop-color="#f4f1ec"/>
        </linearGradient>
      </defs>
      <rect width="468" height="366" fill="url(#beachTones)"/>
    </svg>
    <h2 class="info-title">INFORMATION</h2>
    <div class="info-col info-col--left">
      <p>There will be a 5% discount on rooms booked at the Velunda under the event Owen &amp; Marisa Wedding.</p>
      <p>The resort has a total of 24 rooms it would be nice if the majority of guests could stay at the resort from the night before until the night after the wedding but if you choose to stay elsewhere on the island there are plenty of other places to stay for cheaper and everything is fairly close as its a small island.</p>
    </div>
    <div class="info-col info-col--right">
      <p>We have currently blocked room stay for a short period of time so our guests can book rooms.</p>
      <p>If you choose to do so please email reservations@velundastays.example. Once rooms become available to the public again, towards the end of Jan, it will be first come first served basis.</p>
      <p>The resort is very popular so im assuming once this happens the rooms will be booked out.</p>
    </div>
    <p class="line website">If you would like to check out the resort itself the website is www.velundagrand-isle.example</p>
    <p class="closing">We know its a fair distance to travel but we would really love to see you all there to celebrate and maybe even enjoy a small holiday while you're here its a beautiful part of the world. If anyone has any questions please feel free to contact Owen on 0431907254</p>
  </section>
</main>
</body>
</html>
```